Corporate Identity,Logo,Clothing,Letterhead,Business Cards,Signage etc

Name of Business - Kellaway & Brune Crash Repairs
Colours - Royal Blue, White & Yellow

Industry/Entity Type

Business

```html
<!DOCTYPE html>
<html lang="en">
<head>
<meta charset="utf-8">
<title>Kellaway &amp; Brune Crash Repairs – Stationery</title>
<link rel="stylesheet" href="https://fonts.googleapis.com/css2?family=Exo+2:wght@500;800&display=swap">
<style>
  :root {
    --backdrop: #d8e1e7;
    --paper: #ffffff;
    --paper-edge: #a9b3c8;
    --royal-blue: #2b3990;
    --yellow: #fbb040;
  }
  * { margin: 0; padding: 0; box-sizing: border-box; }
  html, body { width: 1200px; height: 1000px; overflow: hidden; }
  body {
    background: var(--backdrop);
    position: relative;
    font-family: "Exo 2", "Segoe UI", sans-serif;
    color: var(--royal-blue);
  }
  .sheet {
    position: absolute;
    background: var(--paper);
    border: 1px solid var(--paper-edge);
  }
  .letterhead { left: 438px; top: 105px; width: 550px; height: 774px; }
  .business-card { left: 233px; top: 243px; width: 400px; height: 245px; }
  .envelope { left: 30px; top: 521px; width: 772px; height: 295px; }

  /* compact brand mark: initials beside a yellow square */
  .brand-mark {
    position: absolute;
    display: flex;
    align-items: center;
    gap: 4px;
    height: 40px;
  }
  .brand-mark .initials {
    font-weight: 800;
    font-size: 24px;
    line-height: 1;
    letter-spacing: 0.5px;
    color: var(--royal-blue);
  }
  .brand-mark .square {
    width: 16px;
    height: 16px;
    background: var(--yellow);
  }

  .brand-name {
    position: absolute;
    line-height: 1;
    white-space: nowrap;
  }
  .brand-name .name {
    display: block;
    font-weight: 800;
    font-size: 18px;
    letter-spacing: 1px;
    text-transform: uppercase;
  }
  .brand-name .trade {
    display: block;
    font-weight: 500;
    font-size: 17px;
    letter-spacing: 0.5px;
    margin-top: 2px;
  }

  .letterhead .brand-mark { left: 29px; top: 28px; }
  .letterhead .brand-name { left: 110px; top: 34px; }

  .business-card .brand-mark { left: 0; right: 0; top: 72px; justify-content: center; height: 36px; }
  .business-card .brand-mark .initials { font-size: 21px; }
  .business-card .brand-mark .square { width: 14px; height: 14px; }
  .business-card .brand-name { left: 0; right: 0; top: 130px; text-align: center; }
  .business-card .brand-name .trade { font-size: 20px; margin-top: 4px; }

  .envelope .brand-mark { left: 689px; top: 15px; }
  .envelope .brand-name { left: 23px; top: 16px; }
  .envelope .brand-name .trade { font-size: 19px; margin-top: 4px; }

  /* large corner feature */
  .feature-name {
    position: absolute;
    left: 850px;
    top: 790px;
    width: 300px;
    font-weight: 800;
    font-size: 50px;
    line-height: 1.05;
    letter-spacing: 1px;
    text-transform: uppercase;
    color: var(--royal-blue);
  }
  .feature-square {
    position: absolute;
    left: 1030px;
    top: 670px;
    width: 95px;
    height: 95px;
    background: var(--yellow);
  }
</style>
</head>
<body>
  <section class="sheet letterhead">
    <div class="brand-mark"><span class="initials">K&amp;B</span><span class="square"></span></div>
    <div class="brand-name">
      <span class="name">Kellaway &amp; Brune</span>
      <span class="trade">Crash Repairs</span>
    </div>
  </section>

  <section class="sheet business-card">
    <div class="brand-mark"><span class="initials">K&amp;B</span><span class="square"></span></div>
    <div class="brand-name">
      <span class="name">Kellaway &amp; Brune</span>
      <span class="trade">Crash Repairs</span>
    </div>
  </section>

  <section class="sheet envelope">
    <div class="brand-name">
      <span class="name">Kellaway &amp; Brune</span>
      <span class="trade">Crash Repairs</span>
    </div>
    <div class="brand-mark"><span class="initials">K&amp;B</span><span class="square"></span></div>
  </section>

  <span class="feature-square"></span>
  <div class="feature-name">Kellaway &amp; Brune</div>
</body>
</html>
```